■ 依頼の目的/概要

当社は自宅を拠点とした個人営業(女性訓練士)のドッグスクールです。看板や名刺に使用できるようなロゴマーク の作成を依頼します。

■ ロゴマークにしたい社名・店名・サイト名

社名は「柚原ドッグスクール」(所在地からつけた名称です)

■ ロゴマークにする会社・お店・サイトの特徴やアピールポイント

一番メインの仕事は犬のしつけです。しつけといっても、オスワリやマテを教える学校というより、「いつまでも吠え続ける」「飼い主を咬む」などといった、問題行動を出張訓練で解決することを専門としています。

弊社HPはこちらです↓
http://www.yuharawanko.jp/

■ ロゴマークに希望すること(雰囲気・色・イメージなど)

女性(20代~50代)が親しみやすく、信頼してもらえるようなイメージを想定しています。色は視認性を良くしたいのですが、蛍光色のようなものは避けたいと思います。女性訓練士であることをイメージできるようなデザインであればなお良いです。

■ 納品ファイルの希望

イラストレーター形式/フォトショップ形式のいづれか

■ 利用用途

看板/名刺/ウェブサイト/

今回のロゴマークの主な用途は自宅の事務所部分(木枠の部分)の壁面上部へ設置する看板への使用となります。

看板サイズ W1800mm×H600mm~900mm

ロゴマークのほかに、営業品目(出張訓練、ドッグホテル)、電話番号、HPのURLを入れたいですが、サイズ的に無理があればURLは入れなくてもかまいません。

■ その他/注意点

選択させて頂いたロゴマークの著作権(財産権)等の扱いはQuillo利用規約に従い、弊社に譲渡をお願いします。フォントや画像素材などを利用する場合は上記利用用途に使用できることを確認し、第三者の知的財産権等に注意して下さい。
看板サイズの記載が間違っていました

幅2400mm~H900mmの誤りでした、訂正します
色について書き忘れがありましたので追記します。
看板は白を基調として、その上に文字とロゴをデザインしていただきたいと思います、大事なことを書き忘れていてすみません、よろしくお願いいたします。
沢山の提案をいただき、ありがとうございました。
以下の点を追加して依頼を延長したいと思います、よろしくお願いいたします。

看板の目的
1.住宅街にあるため、どこがスクールなのかわからず、通り過ぎてしまうお客様がとても多いので、「ここが柚原ドッグスクールですよ!」と走っている車からも認識できるようにしたい。

2.何気なく看板を目にした人が、「ここは何か、犬に関することをしている場所?」と注意を引くものにしたい。とくに、犬を飼っている人に対してアピールするものであってほしい。

3.トレーニングを依頼してくる人の大半は、20代後半~50代の既婚女性であるため、親しみやすいが、かわいらしすぎないものであってほしい。

希望する色、デザインについて
1.使用する色は、文字も含めて、白、グレー、赤(濃い色)、黒(または濃いグレー)、でお願いします。

2.柚原ドッグスクールの文字は、看板の半分程度を占める大きさであること、「出張訓練」「ドッグホテル」「電話番号」は全体のデザインのバランスでお願いします。

3.看板のサイズの都合上、URL、その他の文字は使わない方針でいきたいと思います。
沢山のご提案、ありがとうございます!

色などはっきり指定したせいか、自分のイメージに近い提案を次々といただき、どれもいいデザインで、甲乙つけがたく思っています。住宅街なので、景観に対してあまりにも目立つのも気が引ける、でも視認性が弱すぎると看板の意味がないし・・・と自分自身でも悩みながらの依頼になっています。残り短い時間ですが、よろしくお願いいたします。
■ 選んだ理由

小さい画像で見たときに、はっきりとドッグスクールの文字が読めること、文字とロゴの組み合わせが明るく、楽しそうな雰囲気をもっていること、年齢を問わず親しみやすさがあること、が決め手になりました。

■ 提案者全員へのお礼・コメント

デザイン的に気に入ったものが多数あり、最後まで選定に悩みました。沢山のご提案をいただき、本当にありがとうございました。

```html
<!DOCTYPE html>
<html lang="ja">
<head>
<meta charset="utf-8">
<title>柚原ドッグスクール 看板案</title>
<link rel="stylesheet" href="https://fonts.googleapis.com/css2?family=Noto+Sans+JP:wght@500;700;900&display=swap">
<style>
:root{
  --red:#b31b1f;
  --black:#1a1a1a;
  --gray:#8a8a8a;
  --light:#d9d9d9;
  --white:#ffffff;
}
*{margin:0;padding:0;box-sizing:border-box}
html,body{width:851px;height:1200px;overflow:hidden;background:var(--white)}
body{position:relative;font-family:"Noto Sans JP",sans-serif;color:var(--black)}
.sign{position:absolute;left:39px;width:773px;height:366px;border:2px solid var(--light);background:var(--white);overflow:hidden}
.sign--a{top:174px}
.sign--b{top:724px}
.abs{position:absolute}
.title{font-weight:900;letter-spacing:-1px;line-height:1;white-space:nowrap}
.services{list-style:none}
.service{display:flex;align-items:center;gap:8px;font-weight:700;font-size:26px;white-space:nowrap}
.paw{width:26px;height:24px}
.tel-label{font-weight:900;font-size:28px;display:flex;align-items:center;justify-content:center}
.tel-number{font-weight:700;font-size:50px;line-height:52px;letter-spacing:1px;white-space:nowrap}
.mascot{border-radius:4px}

/* variant A */
.sign--a .band-top{left:0;top:10px;width:773px;height:96px;background:var(--red)}
.sign--a .title-plate{left:22px;top:22px;width:530px;height:72px;background:var(--white);border-radius:4px;display:flex;align-items:center;padding-left:18px}
.sign--a .title{font-size:54px}
.sign--a .rule-gray{left:0;top:114px;width:773px;height:4px;background:var(--gray)}
.sign--a .rule-red{left:0;top:122px;width:773px;height:3px;background:var(--red)}
.sign--a .services{left:40px;top:160px;display:flex;gap:60px;color:var(--black)}
.sign--a .paw{fill:var(--red)}
.sign--a .tel-label{left:22px;top:222px;width:82px;height:52px;background:var(--black);color:var(--white)}
.sign--a .tel-number{left:125px;top:222px;color:var(--red)}
.sign--a .band-bottom{left:0;top:316px;width:773px;height:22px;background:var(--red)}
.sign--a .mascot{left:570px;top:30px;width:190px;height:280px;background:linear-gradient(180deg,#f4f4f4,#dedede)}

/* variant B */
.sign--b .title{left:30px;top:22px;font-size:72px;color:var(--black);text-shadow:3px 3px 0 var(--light)}
.sign--b .band{left:0;top:118px;width:640px;height:200px;background:var(--red)}
.sign--b .services{left:30px;top:142px;display:flex;gap:50px;color:var(--white)}
.sign--b .paw{fill:var(--white)}
.sign--b .tel-label{left:30px;top:204px;width:82px;height:52px;background:var(--white);color:var(--red)}
.sign--b .tel-number{left:130px;top:204px;color:var(--white)}
.sign--b .rule-gray{left:0;top:326px;width:773px;height:4px;background:var(--gray)}
.sign--b .mascot{left:600px;top:112px;width:160px;height:240px;background:linear-gradient(180deg,#f4f4f4,#dedede)}
</style>
</head>
<body>

<svg width="0" height="0" style="position:absolute" aria-hidden="true">
  <symbol id="paw-icon" viewBox="0 0 26 24">
    <ellipse cx="13" cy="16" rx="7" ry="6"/>
    <circle cx="5" cy="9" r="3"/>
    <circle cx="10" cy="4" r="3"/>
    <circle cx="16" cy="4" r="3"/>
    <circle cx="21" cy="9" r="3"/>
  </symbol>
</svg>

<section class="sign sign--a">
  <div class="abs band-top"></div>
  <div class="abs title-plate"><h1 class="title">柚原ドッグスクール</h1></div>
  <div class="abs rule-gray"></div>
  <div class="abs rule-red"></div>
  <ul class="abs services">
    <li class="service"><svg class="paw"><use href="#paw-icon"/></svg>出張トレーニング</li>
    <li class="service"><svg class="paw"><use href="#paw-icon"/></svg>ペットホテル</li>
  </ul>
  <div class="abs tel-label">TEL</div>
  <div class="abs tel-number">011-555-0142</div>
  <div class="abs band-bottom"></div>
  <div class="abs mascot" role="img" aria-label="首輪に店名を付けた白い犬が座っているイラスト"></div>
</section>

<section class="sign sign--b">
  <h2 class="abs title">柚原ドッグスクール</h2>
  <div class="abs band"></div>
  <ul class="abs services">
    <li class="service"><svg class="paw"><use href="#paw-icon"/></svg>出張トレーニング</li>
    <li class="service"><svg class="paw"><use href="#paw-icon"/></svg>ペットホテル</li>
  </ul>
  <div class="abs tel-label">TEL</div>
  <div class="abs tel-number">011-555-0142</div>
  <div class="abs rule-gray"></div>
  <div class="abs mascot" role="img" aria-label="首輪に店名を付けた白い犬が座っているイラスト"></div>
</section>

</body>
</html>
```